Luxury Tea Brand Needs Packaging Design

Our team needs a luxe design replicating the shape of the attached picture for a box that will contain drawstring teabags. There is an opportunity for silver or gold reflective design

Please include a design for the

Product dimensions - 10.5x4x9 cm
things to keep in mind

- luxury design
- Mainly black with either silver or gold
- Should say pack of 100
- Should say Leaf Harbor Tea Filters

some of our products have been attached as a style reference

website is www.leafharbor.example

Target Market(s)

modern millennials

Requirements
Must have
• luxury feel
Nice to have
• shiny designs

```html
<!DOCTYPE html>
<html lang="en">
<head>
<meta charset="utf-8">
<title>Leaf Harbor Tea Filters – Box Dieline</title>
<link rel="stylesheet" href="https://fonts.googleapis.com/css2?family=Tinos&display=swap">
<style>
  :root {
    --paper: #ffffff;
    --ink-black: #0c0c0a;
    --black-sheen: #24200f;
    --gold-deep: #7f6c1c;
    --gold: #8f7b24;
    --gold-bright: #b59c3a;
    --gold-highlight: #c9b259;
    --gold-label: #8a7621;
  }
  html, body {
    margin: 0;
    padding: 0;
    width: 901px;
    height: 1200px;
    overflow: hidden;
    background: var(--paper);
  }
  .dieline {
    display: block;
    width: 901px;
    height: 1200px;
  }
  .flap { fill: url(#flapSheen); }
  .panel-black { fill: url(#blackLeafTone); }
  .panel-gold { fill: url(#goldLeafTone); }
  .front-label { fill: url(#labelGold); }
  .brand-name {
    font-family: "Tinos", "Times New Roman", serif;
    font-size: 32px;
    fill: var(--ink-black);
    letter-spacing: 1px;
  }
  .pack-count {
    font-family: "Tinos", "Times New Roman", serif;
    font-size: 20px;
    fill: var(--ink-black);
  }
</style>
</head>
<body>
<svg class="dieline" viewBox="0 0 901 1200" xmlns="http://www.w3.org/2000/svg" aria-label="Leaf Harbor Tea Filters box dieline">
  <defs>
    <linearGradient id="blackLeafTone" x1="0" y1="0" x2="1" y2="1">
      <stop offset="0" stop-color="var(--ink-black)"/>
      <stop offset="0.35" stop-color="var(--black-sheen)"/>
      <stop offset="0.55" stop-color="var(--ink-black)"/>
      <stop offset="0.8" stop-color="var(--black-sheen)"/>
      <stop offset="1" stop-color="var(--ink-black)"/>
    </linearGradient>
    <linearGradient id="goldLeafTone" x1="0" y1="0" x2="1" y2="1">
      <stop offset="0" stop-color="var(--gold-deep)"/>
      <stop offset="0.3" stop-color="var(--gold)"/>
      <stop offset="0.5" stop-color="var(--gold-bright)"/>
      <stop offset="0.7" stop-color="var(--gold)"/>
      <stop offset="1" stop-color="var(--gold-deep)"/>
    </linearGradient>
    <linearGradient id="labelGold" x1="0" y1="0" x2="1" y2="1">
      <stop offset="0" stop-color="var(--gold-label)"/>
      <stop offset="0.45" stop-color="var(--gold-bright)"/>
      <stop offset="0.55" stop-color="var(--gold-highlight)"/>
      <stop offset="1" stop-color="var(--gold-label)"/>
    </linearGradient>
    <linearGradient id="flapSheen" x1="0" y1="0" x2="1" y2="0">
      <stop offset="0" stop-color="var(--ink-black)"/>
      <stop offset="0.5" stop-color="#1a1912"/>
      <stop offset="1" stop-color="var(--ink-black)"/>
    </linearGradient>
  </defs>

  <!-- Glue tab -->
  <polygon class="flap glue-tab" points="37,458 75,441 75,756 37,739"/>

  <!-- Back panel -->
  <g role="img" aria-label="Scattered gold tea leaf pattern on black">
    <rect class="panel-black back-panel" x="75" y="441" width="270" height="315"/>
  </g>
  <!-- Bottom panel and tuck -->
  <g role="img" aria-label="Scattered black tea leaf pattern on gold">
    <rect class="panel-gold bottom-panel" x="75" y="756" width="270" height="127"/>
  </g>
  <polygon class="flap bottom-tuck" points="75,883 345,883 336,906 84,906"/>

  <!-- Left side panel -->
  <polygon class="flap side-top-flap" points="345,441 348,381 462,381 462,441"/>
  <g role="img" aria-label="Scattered black tea leaf pattern on gold">
    <rect class="panel-gold side-panel" x="345" y="441" width="117" height="315"/>
  </g>
  <polygon class="flap side-bottom-flap" points="345,756 462,756 462,816 348,816"/>

  <!-- Lid and tuck -->
  <polygon class="flap lid-tuck" points="462,328 470,294 727,294 735,328"/>
  <g role="img" aria-label="Scattered black tea leaf pattern on gold">
    <rect class="panel-gold lid-panel" x="462" y="328" width="273" height="113"/>
  </g>

  <!-- Front panel -->
  <g role="img" aria-label="Scattered gold tea leaf pattern on black">
    <rect class="panel-black front-panel" x="462" y="441" width="273" height="315"/>
  </g>
  <rect class="front-label" x="492" y="471" width="213" height="210"/>
  <text class="brand-name" text-anchor="middle">
    <tspan x="598.5" y="558">Leaf Harbor</tspan>
    <tspan x="598.5" y="596">Tea Filters</tspan>
  </text>
  <text class="pack-count" x="598.5" y="652" text-anchor="middle">pack of 100</text>

  <!-- Right side panel -->
  <polygon class="flap side-top-flap" points="735,441 735,381 852,381 855,441"/>
  <g role="img" aria-label="Scattered black tea leaf pattern on gold">
    <rect class="panel-gold side-panel" x="735" y="441" width="120" height="315"/>
  </g>
  <polygon class="flap side-bottom-flap" points="735,756 855,756 852,816 735,816"/>
</svg>
</body>
</html>
```